Kestrel Bridge Consulting (KBC) Business Card Design

I would like to create double-sided business cards that contain:
1) Name: Derek Molvane
2) Phone Number: +1 (555) 218-4907
3) Email: Derek.Molvane@KestrelBridgeConsulting.example
4) Website: KestrelBridgeConsulting.example

I would like to include my logo and a color scheme similar to the Varnholt Grand Prix Ostera squad color scheme (black, silver, greenish-blue – but can also include regular blue)

What we do: Our company develops and delivers innovative and pragmatic information technology and cybersecurity risk and compliance solutions for organizations in the commercial market as well as the federal, and state/local sectors.

```html
<!DOCTYPE html>
<html lang="en">
<head>
<meta charset="utf-8">
<title>Kestrel Bridge Consulting — Business Card</title>
<link rel="stylesheet" href="https://fonts.googleapis.com/css2?family=Arimo:wght@400;700&display=swap">
<style>
  :root {
    --backdrop: #2b2b2d;
    --card: #2f2f31;
    --card-front: #333336;
    --emboss: #262628;
    --emboss-edge: #3c3c3f;
    --silver: #e9eaec;
    --muted: #c9cacd;
    --teal: #1fc3c0;
    --teal-faint: rgba(31, 195, 192, 0.10);
    --blue: #1f5fae;
    --rule: rgba(233, 234, 236, 0.55);
  }
  * { box-sizing: border-box; margin: 0; padding: 0; }
  html, body {
    width: 1200px;
    height: 689px;
    overflow: hidden;
    background: var(--backdrop);
    font-family: "Arimo", Arial, sans-serif;
  }
  .canvas {
    position: relative;
    width: 1200px;
    height: 689px;
    display: flex;
    align-items: center;
    justify-content: center;
    gap: 40px;
  }
  .card {
    position: relative;
    width: 520px;
    height: 297px;
    border-radius: 14px;
    overflow: hidden;
    box-shadow: 0 14px 34px rgba(0, 0, 0, 0.45);
  }

  /* Back side */
  .card--back {
    background: var(--card);
    display: flex;
    align-items: center;
    justify-content: center;
  }
  .brand {
    display: flex;
    align-items: center;
    gap: 14px;
  }
  .brand__mark {
    width: 44px;
    height: 44px;
    border-radius: 50%;
    flex: none;
  }
  .brand__name {
    font-weight: 400;
    letter-spacing: 0.12em;
    text-transform: uppercase;
    line-height: 1.05;
  }
  .card--back .brand__mark {
    background: var(--emboss);
    box-shadow: 1px 1px 0 var(--emboss-edge);
  }
  .card--back .brand__name {
    font-size: 22px;
    color: var(--emboss);
    text-shadow: 1px 1px 0 var(--emboss-edge);
  }

  /* Front side */
  .card--front {
    background: var(--card-front);
  }
  .front__decor {
    position: absolute;
    left: 10px;
    top: 70px;
    width: 250px;
    height: 250px;
    border-radius: 50%;
    background: var(--teal-faint);
  }
  .card--front .brand {
    position: absolute;
    right: 34px;
    top: 30px;
  }
  .card--front .brand__mark {
    width: 40px;
    height: 40px;
    background: var(--teal);
  }
  .card--front .brand__name {
    font-size: 17px;
    color: var(--silver);
  }
  .front__rule {
    position: absolute;
    left: 200px;
    right: 34px;
    top: 104px;
    height: 1px;
    background: var(--rule);
  }
  .person {
    position: absolute;
    left: 34px;
    top: 152px;
  }
  .person__name {
    font-size: 25px;
    font-weight: 700;
    color: var(--teal);
    line-height: 1.1;
  }
  .person__title {
    font-size: 13px;
    color: var(--muted);
    margin-top: 3px;
  }
  .person__rule {
    position: absolute;
    left: 34px;
    right: 34px;
    top: 212px;
    height: 1px;
    background: var(--rule);
  }
  .contact {
    position: absolute;
    left: 34px;
    top: 222px;
    list-style: none;
  }
  .contact__item {
    display: flex;
    align-items: center;
    gap: 9px;
    font-size: 12.5px;
    color: var(--silver);
    line-height: 20px;
  }
  .contact__icon {
    width: 12px;
    height: 12px;
    flex: none;
    fill: var(--teal);
  }
</style>
</head>
<body>
<main class="canvas">
  <section class="card card--back" aria-label="Card back">
    <div class="brand">
      <span class="brand__mark"></span>
      <p class="brand__name">Kestrel<br>Bridge<br>Consulting</p>
    </div>
  </section>

  <section class="card card--front" aria-label="Card front">
    <div class="front__decor"></div>
    <div class="brand">
      <span class="brand__mark"></span>
      <p class="brand__name">Kestrel<br>Bridge<br>Consulting</p>
    </div>
    <div class="front__rule"></div>

    <div class="person">
      <p class="person__name">Derek Molvane</p>
      <p class="person__title">President</p>
    </div>
    <div class="person__rule"></div>

    <ul class="contact">
      <li class="contact__item">
        <svg class="contact__icon" viewBox="0 0 24 24" aria-hidden="true"><path d="M6.6 10.8a15.1 15.1 0 0 0 6.6 6.6l2.2-2.2a1 1 0 0 1 1-.25 11.4 11.4 0 0 0 3.6.57 1 1 0 0 1 1 1V20a1 1 0 0 1-1 1A17 17 0 0 1 3 4a1 1 0 0 1 1-1h3.5a1 1 0 0 1 1 1c0 1.25.2 2.45.57 3.57a1 1 0 0 1-.25 1z"/></svg>
        +1 (555) 218-4907
      </li>
      <li class="contact__item">
        <svg class="contact__icon" viewBox="0 0 24 24" aria-hidden="true"><path d="M2 5h20v14H2z M3.5 6.5 12 13l8.5-6.5" fill="var(--teal)"/><path d="M3.5 6.5 12 13l8.5-6.5" fill="none" stroke="#333336" stroke-width="1.6"/></svg>
        Derek.Molvane@KestrelBridgeConsulting.example
      </li>
      <li class="contact__item">
        <svg class="contact__icon" viewBox="0 0 24 24" aria-hidden="true"><circle cx="12" cy="12" r="10"/><path d="M2 12h20M12 2c3 3 3 17 0 20M12 2c-3 3-3 17 0 20" fill="none" stroke="#333336" stroke-width="1.4"/></svg>
        www.KestrelBridgeConsulting.example
      </li>
    </ul>
  </section>
</main>
</body>
</html>
```